Corporate Design für Sanfte Nacht Kinderberatung
Vielen Dank für die tolle und unkomplizierte Zusammenarbeit.
Zielgruppe
Wir informieren, trainieren und coachen Eltern darin, wie sie ihre Babies und Kleinkinder zum Schlafen brinen.
Zielgruppe sind alle Eltern, in der Regel Akademiker, deren 0-3 jährigen Kinder Ein- und/oder Durchschlafprobleme haben
Aufgabenstellung
Ich bräuchte bitte Vorschläge mit 2 verschiedenen Namen, da ich in diesem Jahr heiraten werde:
- mein aktueller Name ist Lena Borwitz
- mein künftiger Name ist Lena Saller
- Eventuell kann das CD meine Initialien im Firmennamen beinhalten, wie z.B.: SAnfte nacht kinderberatung (nur eine Idee, auf die ich allerdings nicht festgelegt bin :-)) Ihr wisst das besser
- ich bräuchte bitte auch einen Header für meine bereits existierende Pagora Domain
- das CD sollte nicht zu verspielt sein und kompetent wirken

```html
<!DOCTYPE html>
<html lang="de">
<head>
<meta charset="utf-8">
<title>Sanfte Nacht Kinderberatung – Geschäftsausstattung</title>
<link rel="stylesheet" href="https://fonts.googleapis.com/css2?family=Ubuntu:wght@400;500&family=Arimo:wght@400;700&display=swap">
<style>
  :root {
    --bg: #e9e7e4;
    --paper: #ffffff;
    --ink: #4a4a4a;
    --ink-soft: #7a7a7a;
    --brand-blue: #2f95c4;
    --rule: #cfe3ee;
  }
  * { box-sizing: border-box; margin: 0; padding: 0; }
  html, body { width: 1200px; height: 1189px; overflow: hidden; }
  body { background: var(--bg); position: relative; font-family: "Arimo", Arial, sans-serif; color: var(--ink); }

  .sheet, .card { position: absolute; background: var(--paper); box-shadow: 0 2px 8px rgba(0,0,0,.18); overflow: hidden; }

  .brand { font-family: "Ubuntu", sans-serif; font-weight: 500; color: var(--ink); line-height: 1.05; display: flex; align-items: center; gap: 8px; }
  .brand-dot { width: 9px; height: 9px; border-radius: 50%; background: var(--brand-blue); flex: none; }

  /* Briefbogen */
  .letterhead { left: 57px; top: 156px; width: 646px; height: 914px; }
  .letterhead .accent-bar { position: absolute; left: 0; top: 182px; width: 7px; bottom: 0; background: var(--brand-blue); }
  .letterhead .brand { position: absolute; right: 54px; top: 60px; font-size: 25px; width: 230px; text-align: left; }
  .letterhead .sender-line { position: absolute; left: 40px; top: 190px; font-size: 6.5px; color: var(--ink-soft); }
  .letterhead .recipient { position: absolute; left: 40px; top: 208px; font-size: 8.5px; line-height: 12px; color: var(--ink-soft); }
  .letterhead .subject { position: absolute; left: 40px; top: 266px; font-size: 8.5px; color: var(--ink-soft); }
  .letterhead .greeting { position: absolute; left: 40px; top: 300px; font-size: 8.5px; color: var(--ink-soft); }
  .letterhead .body { position: absolute; left: 40px; top: 324px; width: 420px; font-size: 9px; line-height: 9.8px; color: var(--ink-soft); }
  .letterhead .signature { position: absolute; left: 40px; top: 678px; font-size: 8.5px; line-height: 12px; color: var(--ink-soft); }
  .letterhead .footer { position: absolute; left: 50px; right: 40px; top: 864px; border-top: 1px solid var(--rule); padding-top: 6px; display: grid; grid-template-columns: 1.3fr 1.3fr 1.3fr 1.5fr; font-size: 5.5px; line-height: 7px; font-weight: 700; color: var(--ink); }

  /* Visitenkarten */
  .card { width: 372px; height: 239px; }
  .card .brand { position: absolute; left: 40px; top: 40px; font-size: 19px; width: 180px; }
  .card .contact { font-family: "Ubuntu", sans-serif; font-size: 10px; line-height: 12px; color: var(--ink); }
  .card .contact .gap { height: 5px; }
  .card .name { font-family: "Ubuntu", sans-serif; font-weight: 500; font-size: 14px; color: var(--brand-blue); }
  .card .role { font-family: "Ubuntu", sans-serif; font-size: 7px; color: var(--ink); margin-top: 3px; }

  .card-front-a { left: 740px; top: 158px; }
  .card-front-a .contact { position: absolute; left: 46px; top: 129px; }
  .card-front-a .person { position: absolute; left: 214px; top: 122px; }

  .card-front-b { left: 740px; top: 477px; }
  .card-front-b .divider { position: absolute; left: 208px; top: 82px; width: 2px; height: 140px; background: var(--rule); }
  .card-front-b .person { position: absolute; left: 218px; top: 84px; }
  .card-front-b .contact { position: absolute; left: 218px; top: 140px; }

  .card-back { left: 740px; top: 807px; display: flex; align-items: center; justify-content: center; }
  .card-back .brand { position: static; font-size: 24px; width: 220px; }
</style>
</head>
<body>

<article class="sheet letterhead">
  <div class="accent-bar"></div>
  <div class="brand"><span class="brand-dot"></span><span>Sanfte Nacht Kinderberatung</span></div>
  <div class="sender-line">Max Mustermann Beispielstraße 38 12345 Beispielort</div>
  <div class="recipient">Beispielfirma GmbH<br>Firmenstraße 12<br>12345 Firmenort</div>
  <div class="subject">Betreffzeile</div>
  <div class="greeting">Sehr geehrte Damen und Herren,</div>
  <div class="body">
    <p>Lorem ipsum dolor sit amet, consetetur sadipscing elitr, sed diam nonumy eirmod tempor invidunt ut labore et dolore magna aliquyam erat, sed diam voluptua. At vero eos et accusam et justo duo dolores et ea rebum. Stet clita kasd gubergren, no sea takimata sanctus est Lorem ipsum dolor sit amet. Lorem ipsum dolor sit amet, consetetur sadipscing elitr, sed diam nonumy eirmod tempor invidunt ut labore et dolore magna aliquyam erat, sed diam voluptua. At vero eos et accusam et justo duo dolores et ea rebum. Stet clita kasd gubergren, no sea takimata sanctus est Lorem ipsum dolor sit amet. Lorem ipsum dolor sit amet, consetetur sadipscing elitr, sed diam nonumy eirmod tempor invidunt ut labore et dolore magna aliquyam erat, sed diam voluptua. At vero eos et accusam et justo duo dolores et ea rebum. Stet clita kasd gubergren, no sea takimata sanctus est Lorem ipsum dolor sit amet.<br>Duis autem vel eum iriure dolor in hendrerit in vulputate velit esse molestie consequat, vel illum dolore eu feugiat nulla facilisis at vero eros et accumsan et iusto odio dignissim qui blandit praesent luptatum zzril delenit augue duis dolore te feugait nulla facilisi. Lorem ipsum dolor sit amet, consectetuer adipiscing elit, sed diam nonummy nibh euismod tincidunt ut laoreet dolore magna aliquam erat volutpat.<br>Ut wisi enim ad minim veniam, quis nostrud exerci tation ullamcorper suscipit lobortis nisl ut aliquip ex ea commodo consequat. Duis autem vel eum iriure dolor in hendrerit in vulputate velit esse molestie consequat, vel illum dolore eu feugiat nulla facilisis at vero eros et accumsan et iusto odio dignissim qui blandit praesent luptatum zzril delenit augue duis dolore te feugait nulla facilisi.<br>At vero eos et accusam et justo duo dolores et ea rebum. Stet clita kasd gubergren, no sea takimata sanctus est Lorem ipsum dolor sit amet. Lorem ipsum dolor sit amet, consetetur sadipscing elitr, sed diam nonumy eirmod tempor invidunt ut labore et dolore magna aliquyam erat, sed diam voluptua. At vero eos et accusam et justo duo dolores et ea rebum. Stet clita kasd gubergren, no sea takimata sanctus est Lorem ipsum dolor sit amet. Lorem ipsum dolor sit amet, consetetur sadipscing elitr. At accusam aliquyam diam diam dolore dolores duo eirmod eos erat, et nonumy sed tempor et et invidunt justo labore Stet clita ea et gubergren, kasd magna no rebum. sanctus sea sed takimata ut vero voluptua. est Lorem ipsum dolor sit amet. Lorem ipsum dolor sit amet, consetetur</p>
  </div>
  <div class="signature">Mit freundlichen Grüßen<br><br><br>Max Mustermann<br>Beispielort, 31. Juli 2014</div>
  <footer class="footer">
    <div>Lena Saller<br>Musterstraße 44<br>D-12345 Musterstadt</div>
    <div>Max Mustermann<br>Max Mustermann</div>
    <div>Tel.: 0000-111222<br>Fax: 0000-111223<br>info@muster.de<br>www.muster.de</div>
    <div>Kreisbank Musterstadt<br>IBAN: DE00 1234 5678 0000 0000 00<br>BIC: MUSTDE00XXX</div>
  </footer>
</article>

<section class="card card-front-a">
  <div class="brand"><span class="brand-dot"></span><span>Sanfte Nacht Kinderberatung</span></div>
  <div class="contact">
    Musterstraße 44<br>D-12345 Musterstadt
    <div class="gap"></div>
    Tel:0000-111222<br>Fax:0000-111223
    <div class="gap"></div>
    info@muster.de<br>www.muster.de
  </div>
  <div class="person"><div class="name">Lena Saller</div><div class="role">Berufsbezeichnung</div></div>
</section>

<section class="card card-front-b">
  <div class="brand"><span class="brand-dot"></span><span>Sanfte Nacht Kinderberatung</span></div>
  <div class="divider"></div>
  <div class="person"><div class="name">Lena Saller</div><div class="role">Berufsbezeichnung</div></div>
  <div class="contact">
    Musterstraße 44<br>D-12345 Musterstadt
    <div class="gap"></div>
    Tel:0000-111222<br>Fax:0000-111223
    <div class="gap"></div>
    info@muster.de<br>www.muster.de
  </div>
</section>

<section class="card card-back">
  <div class="brand"><span class="brand-dot"></span><span>Sanfte Nacht Kinderberatung</span></div>
</section>

</body>
</html>
```